12-page Product Brochure for School Archiving Specialist Company

We require a 12-page brochure for our company based in Melbourne, VIC. Our company specializes in tailored archiving solutions for Australian schools of all sizes, and our main product is the "Tidy Vault" archiving system.
We have a ready-to-use brochure structure that can help designers get a better idea of what we're looking for in the final brochure. We will also provide imagery, graphics, and copy that will be used in the brochure - designers will just have to piece them all together and add their own touch of flair to it!
We are looking for the design to clearly communicate what we we do from a product, service and system perspective. The design should inspire trust, be clear and concise, but also to incorporate the fun spirit that embodies our company and our mascots, Pimble and Wexo.
Attached is a suggested brochure structure, previous brochures we have had designed, a project brief, as well as examples of what we like.
Company Name: Tidy Vault (operating under Bramble Files Group)
Company Location: Melbourne, Victoria, Australia
Contacts: perry@bramblefilesgroup.com.au / desmond@bramblefilesgroup.com.au
Project Type: 12-page A4 Brochure
Project Goal: A brochure that clearly communicates what we do from a product, service, and system perspective. The design should inspire trust, be clear and concise, but should also incorporate the fun spirit that embodies our company and our mascots, Pimble and Wex.
Final Output Format: .PDF and .AI or .INDD
Project Details and Scope of Work: We require a 14-page A4 brochure for our company based in Melbourne, VIC. Our company specializes in tailored archiving solutions for Australian schools of all sizes, and our main product is the "Tidy Vault" archiving system. We have a ready-to-use brochure structure that can help designers get a better idea of what we're looking for in the final brochure. We will also provide imagery, graphics, and copy that will be used in the brochure - designers will just have to piece them all together, fill in any gaps, and add their own touch of flair to it!
Links to Existing Content:
Graphics/Imagery*: https://files.example-share.net/folders/a7k2pq91
Brochure Copy:
https://texts.example-share.net/doc/b4m8rz30
Photos:
https://files.example-share.net/folders/c9t3wn57
Previous Tidy Vault Brochures and Best Practice Design Examples Pages**:
https://files.example-share.net/folders/d2h6vx84
* Each folder, named after different sections of the brochure, contains graphics we would like to be used for that corresponding page/section.
** The photos in each folder are examples. Please refer to the Brochure Photo Folder for all options.
Target Market(s)
Schools of all sizes in Australia
Industry/Entity Type
Archiving / Storage
Look and feel

```html
<!DOCTYPE html>
<html lang="en">
<head>
<meta charset="utf-8">
<title>Digitisation &amp; Scanning – Tidy Vault</title>
<link href="https://fonts.googleapis.com/css2?family=Lilita+One&family=Open+Sans:wght@400;600&family=Montserrat:wght@700&family=Bebas+Neue&display=swap" rel="stylesheet">
<style>
  :root {
    --navy: #343d59;
    --navy-deep: #2a3149;
    --green: #6bbf45;
    --green-dark: #4f9a31;
    --red: #e2262b;
    --orange: #e8772a;
    --white: #ffffff;
    --sky: #8fb4dc;
    --quote-grey: #23283a;
    --photo-a: #6f8a68;
    --photo-b: #3f5545;
    --mascot: #9a9ca4;
  }
  * { margin: 0; padding: 0; box-sizing: border-box; }
  html, body { width: 848px; height: 1200px; overflow: hidden; background: var(--navy); }
  .page { position: relative; width: 848px; height: 1200px; overflow: hidden; background: var(--navy); font-family: "Open Sans", sans-serif; }

  .hero-photo { position: absolute; left: 0; top: 0; width: 848px; height: 720px;
    background: linear-gradient(160deg, #8aa07f 0%, var(--photo-a) 35%, var(--photo-b) 75%, #2f3d36 100%); }
  .page-shapes { position: absolute; left: 0; top: 0; }

  .brand { position: absolute; right: 26px; top: 34px; display: flex; align-items: center; gap: 10px;
    font-family: "Lilita One", sans-serif; font-size: 34px; color: var(--white); }
  .brand-square { width: 22px; height: 22px; background: var(--white); }

  .title-banner { position: absolute; left: 118px; top: 214px; width: 628px; height: 140px; }
  .title-text { position: absolute; left: 178px; top: 222px; font-family: "Lilita One", sans-serif;
    color: var(--white); font-size: 76px; line-height: 62px; letter-spacing: 1px; text-transform: uppercase; }

  .intro { position: absolute; left: 182px; top: 356px; width: 560px; height: 106px; background: var(--navy);
    color: var(--white); font-size: 11.4px; line-height: 17px; padding: 12px 18px; }

  .mascot { position: absolute; left: 684px; top: 528px; width: 142px; height: 222px;
    background: linear-gradient(180deg, var(--mascot), #6e7079); border-radius: 8px; }

  .features { list-style: none; }
  .feature { position: absolute; display: flex; align-items: flex-start; gap: 8px;
    font-family: "Montserrat", sans-serif; font-weight: 700; font-size: 13.4px; line-height: 18px; color: var(--white); }
  .feature svg { flex: none; margin-top: -14px; }
  .feature span { width: 300px; }

  .testimonial-word { position: absolute; left: 60px; top: 990px; font-family: "Lilita One", sans-serif;
    font-size: 190px; color: var(--quote-grey); opacity: .6; letter-spacing: 6px; white-space: nowrap; }
  .quote-mark { position: absolute; font-family: "Lilita One", sans-serif; font-size: 200px; line-height: 1; color: var(--quote-grey); }
  .quote-open { left: 26px; top: 990px; }
  .quote-close { left: 760px; top: 1080px; }
  .quote { position: absolute; left: 104px; top: 1010px; width: 650px; text-align: center;
    font-family: "Bebas Neue", sans-serif; font-size: 15.6px; line-height: 18.6px; color: var(--white); letter-spacing: .3px; }
  .quote-source { position: absolute; right: 100px; top: 1158px; text-align: right; }
  .quote-school { font-family: "Montserrat", sans-serif; font-weight: 700; font-size: 14px; color: var(--sky); }
  .quote-person { font-size: 14px; color: var(--sky); }
</style>
</head>
<body>
<div class="page">
  <div class="hero-photo" role="img" aria-label="Photo of a smiling staff member on the phone at a desk with a shaggy dog beside her"></div>

  <svg class="page-shapes" width="848" height="1200" viewBox="0 0 848 1200" aria-hidden="true">
    <polygon points="0,640 560,560 0,720" fill="#24303a" opacity=".55"/>
    <polygon points="0,720 848,560 848,1200 0,1200" fill="var(--navy)"/>
    <polygon points="740,520 848,500 848,600 740,620" fill="var(--navy)"/>
    <polygon points="548,0 634,0 591,70" fill="var(--red)"/>
    <polygon points="634,0 716,0 675,56" fill="var(--green)"/>
    <polygon points="660,0 848,0 848,130 700,130" fill="var(--navy)"/>
  </svg>

  <div class="brand"><span class="brand-square"></span>Tidy Vault</div>

  <svg class="title-banner" viewBox="0 0 628 140" aria-hidden="true">
    <polygon points="50,0 628,0 628,128 0,128 0,40" fill="var(--green)"/>
    <polygon points="0,40 50,0 50,30" fill="var(--green-dark)"/>
    <rect x="0" y="128" width="628" height="5" fill="var(--orange)"/>
  </svg>
  <h1 class="title-text">Digitisation<br>&amp; Scanning</h1>

  <p class="intro">Digitizing your school's archives saves space, reduces waste, and is easy as teaching a dog a new trick. Easily scan and store student records, freeing up physical space and improving access to important information. Make the switch and enjoy the benefits of an organized and eco-friendly record-keeping system!</p>

  <div class="mascot" role="img" aria-label="Illustration of the grey mascot dog holding an x-ray panel"></div>

  <ul class="features">
    <li class="feature" style="left:28px;top:770px">
      <svg width="92" height="44" viewBox="0 0 92 44"><polygon points="14,0 92,0 78,44 0,44" fill="var(--green)"/><path d="M28 22 L40 34 L64 6" stroke="var(--white)" stroke-width="7" fill="none"/></svg>
      <span>Project based or ongoing basis</span></li>
    <li class="feature" style="left:28px;top:830px">
      <svg width="92" height="44" viewBox="0 0 92 44"><polygon points="14,0 92,0 78,44 0,44" fill="var(--green)"/><path d="M28 22 L40 34 L64 6" stroke="var(--white)" stroke-width="7" fill="none"/></svg>
      <span>Wide range of formats including documents, books, plans, wide/large wide format and other historical items</span></li>
    <li class="feature" style="left:28px;top:914px">
      <svg width="92" height="44" viewBox="0 0 92 44"><polygon points="14,0 92,0 78,44 0,44" fill="var(--green)"/><path d="M28 22 L40 34 L64 6" stroke="var(--white)" stroke-width="7" fill="none"/></svg>
      <span>Easily uploaded to VaultDesk or a schools own IT infrastructure</span></li>
    <li class="feature" style="left:426px;top:790px">
      <svg width="92" height="44" viewBox="0 0 92 44"><polygon points="14,0 92,0 78,44 0,44" fill="var(--green)"/><path d="M28 22 L40 34 L64 6" stroke="var(--white)" stroke-width="7" fill="none"/></svg>
      <span>OCR / ICR and AI data capture capabilities</span></li>
    <li class="feature" style="left:426px;top:864px">
      <svg width="92" height="44" viewBox="0 0 92 44"><polygon points="14,0 92,0 78,44 0,44" fill="var(--green)"/><path d="M28 22 L40 34 L64 6" stroke="var(--white)" stroke-width="7" fill="none"/></svg>
      <span>Wide range of output formats including PDF/A, PNG, JPG, JSON</span></li>
  </ul>

  <div class="testimonial-word" aria-hidden="true">Testimonial</div>
  <div class="quote-mark quote-open" aria-hidden="true">&ldquo;</div>
  <div class="quote-mark quote-close" aria-hidden="true">&rdquo;</div>

  <blockquote class="quote">Our school was established in 1967 and over the years our collection of student files had steadily grown to the point where they were becoming burdensome and we were running out of space... Due to the permanent and sensitive nature of the student records it was decided that digitisation, followed by ongoing storage would be the best option for long term preservation and management. Over a period of 6 months 10,000 student records were digitised, quality checked and safely returned to us as high quality archival standard PDFs - no mean feat considering a large portion of our files were very old yellow carbon papers!</blockquote>

  <div class="quote-source">
    <div class="quote-school">Ridgeway College</div>
    <div class="quote-person">Martin Hale, Deputy Principal</div>
  </div>
</div>
</body>
</html>
```